Casa Vero Inspections Business Card

I need a business card for my new company. The company is going to provide home inspections. The name of the company is Casa Vero Inspections. I am not sure if I want a single sided card or a double. I have a logo already that I want to incorporate into the card design. I was wondering if I should incorporate a catch phrase on my card or not. If I did the phrase would be "The Intelligent Choice for Home Inspections" but i am unsure how or if to use it on a card. The following information needs to be on the card.
Home Inspection
My Name: Marcus T. Wolford Phone Number: 555-301-7762 Email: mwolford@casaveroinspections.com Website: www.casaveroinspections.com NY HI License # 27300519462

```html
<!DOCTYPE html>
<html lang="en">
<head>
<meta charset="utf-8">
<title>Casa Vero Inspections – Business Card</title>
<link href="https://fonts.googleapis.com/css2?family=Montserrat:wght@400;500;700&display=swap" rel="stylesheet">
<style>
  :root {
    --backdrop: #2a2c30;
    --card-dark: #060606;
    --card-light: #ffffff;
    --brand-blue: #1665a9;
    --accent-blue: #5cb6ea;
    --text-light: #f2f2f2;
    --text-muted: #d6d6d6;
  }
  * { box-sizing: border-box; margin: 0; padding: 0; }
  html, body {
    width: 1200px;
    height: 825px;
    overflow: hidden;
    background: var(--backdrop);
    font-family: "Montserrat", sans-serif;
  }
  .canvas {
    position: relative;
    width: 1200px;
    height: 825px;
    display: flex;
    align-items: center;
    justify-content: center;
    gap: 40px;
  }
  .card {
    position: relative;
    width: 540px;
    height: 309px;
    border-radius: 30px;
    overflow: hidden;
  }
  /* Back: contact side */
  .card--contact {
    background: var(--card-dark);
    color: var(--text-light);
  }
  .holder {
    position: absolute;
    left: 40px;
    top: 38px;
  }
  .holder__name {
    font-size: 22px;
    font-weight: 500;
    color: var(--accent-blue);
    letter-spacing: 0.2px;
  }
  .holder__license {
    margin-top: 6px;
    font-size: 11.5px;
    font-weight: 500;
    color: var(--text-light);
  }
  .contact-list {
    position: absolute;
    left: 40px;
    top: 132px;
    list-style: none;
  }
  .contact-list__item {
    display: flex;
    align-items: center;
    gap: 10px;
    font-size: 12.5px;
    color: var(--text-muted);
    line-height: 1;
    margin-bottom: 10px;
  }
  .contact-list__icon {
    width: 12px;
    height: 12px;
    flex: none;
    fill: none;
    stroke: var(--accent-blue);
    stroke-width: 1.6;
  }
  .wordmark {
    position: absolute;
    display: flex;
    align-items: center;
    gap: 12px;
    font-weight: 700;
    line-height: 1.05;
  }
  .wordmark__square {
    width: 18px;
    height: 18px;
    flex: none;
  }
  .wordmark--contact {
    right: 40px;
    bottom: 52px;
    font-size: 26px;
    color: var(--text-light);
  }
  .wordmark--contact .wordmark__square { background: var(--accent-blue); }

  /* Front: brand side */
  .card--brand {
    background: var(--card-light);
    box-shadow: 0 4px 0 #d9d9d9, 0 8px 0 #bfbfbf;
  }
  .brand-block {
    position: absolute;
    inset: 0;
    display: flex;
    flex-direction: column;
    align-items: center;
    justify-content: center;
    gap: 26px;
  }
  .wordmark--brand {
    position: static;
    font-size: 34px;
    color: var(--brand-blue);
  }
  .wordmark--brand .wordmark__square { background: var(--brand-blue); width: 22px; height: 22px; }
  .brand-block__rule {
    width: 300px;
    height: 2px;
    background: var(--accent-blue);
  }
  .brand-block__web {
    font-size: 17px;
    font-weight: 500;
    color: var(--accent-blue);
  }
</style>
</head>
<body>
<main class="canvas">
  <section class="card card--contact" aria-label="Card back with contact details">
    <div class="holder">
      <h1 class="holder__name">Marcus T. Wolford</h1>
      <p class="holder__license">NY HI License # 27300519462</p>
    </div>
    <ul class="contact-list">
      <li class="contact-list__item">
        <svg class="contact-list__icon" viewBox="0 0 12 12" aria-hidden="true"><path d="M2.5 1 L4.5 1 L5.2 3.5 L4 4.6 Q5 7 7.4 8 L8.5 6.8 L11 7.5 L11 9.5 Q10.5 11 9 11 Q1 10 1 3 Q1 1.5 2.5 1Z"/></svg>
        555-301-7762
      </li>
      <li class="contact-list__item">
        <svg class="contact-list__icon" viewBox="0 0 12 12" aria-hidden="true"><rect x="1" y="2.5" width="10" height="7"/><path d="M1 2.5 L6 6.5 L11 2.5"/></svg>
        mwolford@casaveroinspections.com
      </li>
      <li class="contact-list__item">
        <svg class="contact-list__icon" viewBox="0 0 12 12" aria-hidden="true"><circle cx="6" cy="6" r="5"/><ellipse cx="6" cy="6" rx="2.2" ry="5"/><path d="M1 6 H11"/></svg>
        www.casaveroinspections.com
      </li>
    </ul>
    <div class="wordmark wordmark--contact">
      <span class="wordmark__square" aria-hidden="true"></span>
      <span class="wordmark__name">Casa Vero<br>Inspections</span>
    </div>
  </section>

  <section class="card card--brand" aria-label="Card front with company name">
    <div class="brand-block">
      <div class="wordmark wordmark--brand">
        <span class="wordmark__square" aria-hidden="true"></span>
        <span class="wordmark__name">Casa Vero Inspections</span>
      </div>
      <span class="brand-block__rule" aria-hidden="true"></span>
      <p class="brand-block__web">www.casaveroinspections.com</p>
    </div>
  </section>
</main>
</body>
</html>
```